Oil & Gas companies needs print design panels for Australia's biggest conference of 2016!

We need artwork design for 2 companies that are linked from Perth, Western Australia (KLV and Dorivel). Logos (in EPS format) have been attached.

Our websites (so that you can get a feel for what we do) are:
www.fenbrookmarq.com
www.dorivel.com

We need two panels for our stand at the TRUMB conference in Brisbane. An image of the stand setup has been provided in the attached images. The panel artwork sizes required are:
1x 985mm x 2349mm h
1x 2349mm x 985mm h

A copy of the guidelines that need to be followed in order to have the artwork correctly displayed have also been attached.

WORDING FOR PANELS

KLV (logo) – panel
TAG LINE: KLV. Your Partner for Success.
Completions and Commissioning,
Operational Readiness
Specialist Inspections,
Whatever your projects requirements,
Wherever you operate,
Whatever your schedule.
KLV helps you achieve project success.

Dorivel (logo) – panel
TAG LINE: Keep your assets under control.
Maintain plant safety.
Avoid unplanned downtime.
Comply with complex regulatory requirements.
Dorivel Hazardous Area and specialist inspection services.
Your Asset. Our Protection.

We need to x2 pics (from the ones supplied/or ones to do with Oil & Gas industry)

Target Market(s)

Conference
Oil & Gas professionals

Industry/Entity Type

Oil And Gas

Font styles to use
Sans Serif
Other font styles liked:
• DIN Offc

Requirements
Must have
• KLV & Dorivel Logo (one per panel)
• Must follow the attached guidelines provided from TRUMB.
• The KLV panel must be engaging and draw clients towards our stand as it is the first thing they will see when entering the conference.
• KLV & Dorivel colours:
• orange = #D76927, R-215 G-105 B-39, CMYK C-11.65 M-70.4 Y-100 K-1.52
• Blue = #21224B, R-33 G-34 B-75, CMYK C-95.65, M-92.65 Y-39.82, K40.01
Nice to have
• We would like to see some examples of faded pictures with wording more predominant.
• KLV:
• Completions and Commissioning - pop out/bold/stand out
• Operational Readiness - pop out/bold/stand out
• Inspections - pop out/bold/stand out
• Dorivel:
• Hazardous Area - pop out/bold/standout
Should not have
• Combined KLV/Dorivel panels - need to be separate

```html
<!DOCTYPE html>
<html lang="en">
<head>
<meta charset="utf-8">
<title>KLV Integrated Solutions – Conference Panel</title>
<link rel="stylesheet" href="https://fonts.googleapis.com/css2?family=Roboto+Condensed:wght@400;700&display=swap">
<style>
  :root {
    --brand-orange: #d76927;
    --brand-orange-mid: #c85a1e;
    --brand-orange-deep: #9a3d10;
    --brand-orange-dark: #5e2206;
    --brand-orange-glow: #ffc27a;
    --brand-navy: #21224b;
    --paper: #ffffff;
    --text-light: #ffffff;
  }
  * { margin: 0; padding: 0; box-sizing: border-box; }
  html, body {
    width: 1200px;
    height: 2860px;
    overflow: hidden;
    background: var(--paper);
  }
  .panel {
    position: relative;
    width: 1200px;
    height: 2860px;
    background: var(--paper);
    font-family: "Roboto Condensed", "Arial Narrow", sans-serif;
  }
  .brand {
    position: absolute;
    top: 34px;
    left: 0;
    width: 100%;
    text-align: center;
    color: var(--brand-navy);
  }
  .brand-name {
    display: block;
    font-size: 196px;
    font-weight: 700;
    line-height: 1;
    letter-spacing: 12px;
  }
  .brand-descriptor {
    display: block;
    margin-top: 18px;
    font-size: 34px;
    font-weight: 700;
    letter-spacing: 3px;
  }
  .hero {
    position: absolute;
    top: 340px;
    left: 8px;
    width: 1184px;
    height: 2520px;
    background: var(--brand-orange);
    overflow: hidden;
  }
  .scene-photo {
    position: absolute;
    left: 0;
    bottom: 0;
    width: 100%;
    height: 1180px;
    background:
      linear-gradient(to bottom, rgba(94,34,6,0) 88%, rgba(94,34,6,0.85) 93%, rgba(154,61,16,0.9) 100%),
      radial-gradient(ellipse 55% 7% at 55% 87%, rgba(255,214,150,0.95) 0%, rgba(255,194,122,0) 100%),
      radial-gradient(ellipse 20% 14% at 88% 80%, rgba(255,200,130,0.7) 0%, rgba(255,194,122,0) 100%),
      radial-gradient(ellipse 14% 16% at 46% 80%, rgba(255,200,130,0.55) 0%, rgba(255,194,122,0) 100%),
      linear-gradient(to bottom, rgba(94,34,6,0) 70%, rgba(94,34,6,0.75) 84%, rgba(94,34,6,0.6) 88%),
      radial-gradient(ellipse 45% 12% at 80% 48%, rgba(240,170,110,0.45) 0%, rgba(240,170,110,0) 100%),
      linear-gradient(to bottom, var(--brand-orange) 0%, var(--brand-orange-mid) 45%, var(--brand-orange-deep) 80%, var(--brand-orange-dark) 100%);
  }
  .headline {
    position: relative;
    z-index: 1;
    padding-top: 155px;
    text-align: center;
    font-weight: 700;
    font-size: 128px;
    line-height: 148px;
  }
  .headline-lead { display: block; color: var(--brand-navy); }
  .headline-accent { display: block; color: var(--text-light); }
  .service-list {
    position: absolute;
    z-index: 1;
    top: 634px;
    left: 204px;
    list-style: none;
    color: var(--text-light);
    font-weight: 700;
    font-size: 52px;
    line-height: 116px;
  }
</style>
</head>
<body>
  <main class="panel">
    <header class="brand">
      <span class="brand-name">KLV</span>
      <span class="brand-descriptor">INTEGRATED SOLUTIONS</span>
    </header>

    <section class="hero">
      <div class="scene-photo" role="img" aria-label="Faded orange-toned photograph of an oil refinery lit up at night beside water, with tall stacks and drifting smoke"></div>

      <h1 class="headline">
        <span class="headline-lead">Your Partner for</span>
        <span class="headline-accent">Success.</span>
      </h1>

      <ul class="service-list">
        <li>Completions and Commissioning,</li>
        <li>Operational Readiness</li>
        <li>Specialist Inspections,</li>
        <li>Whatever your projects requirements,</li>
        <li>Wherever you operate,</li>
        <li>Whatever your schedule.</li>
        <li>KLV helps you achieve project success.</li>
      </ul>
    </section>
  </main>
</body>
</html>
```